Qorvane Management LLC Business Card

The sample logo was attached for the business Card Design for Traffic Control Company named Qorvane Management LLC. Card design needs to have the company logo and colors match the logo color. It will be nice to show some images of Traffic control signs or cones, even roads closer that math the company services

Target Market(s)

Temporary traffic control. Road closer.

Industry/Entity Type

Construction

Contact Information for Business Card

basic information, name, job title, address, email phone, website

Font styles to use
Serif
Sans Serif

Colors
F0912C
F2A743
F7CA91
FBE8D2
FDF5EE
EE7325
F08F49
F5BC92
FAE3D3
FDF4ED

```html
<!DOCTYPE html>
<html lang="en">
<head>
<meta charset="utf-8">
<title>Qorvane Management LLC – Business Card</title>
<link rel="stylesheet" href="https://fonts.googleapis.com/css2?family=Montserrat:wght@400;500;600;700;800&display=swap">
<style>
  :root{
    --orange:#EE7325;
    --orange-light:#F08F49;
    --orange-pale:#F5BC92;
    --orange-deep:#c9521a;
    --black:#0b0b0b;
    --white:#ffffff;
    --label:#8a8a8a;
    --ink:#111111;
  }
  *{margin:0;padding:0;box-sizing:border-box}
  html,body{width:1200px;height:1200px;overflow:hidden;background:var(--white)}
  body{position:relative;font-family:"Montserrat",Arial,sans-serif;color:var(--ink)}

  .side-label{position:absolute;font-weight:700;font-size:22px;color:var(--label);letter-spacing:.3px}
  .side-label--front{left:105px;top:324px}
  .side-label--back{left:121px;top:849px}

  .card{position:absolute;left:315px;width:581px;height:368px;overflow:hidden;
        box-shadow:0 6px 22px rgba(0,0,0,.22)}
  .card--front{top:157px;background:var(--orange)}
  .card--back{top:684px;height:367px;background:var(--white)}

  /* front */
  .front-divider{position:absolute;left:423px;top:0;width:5px;height:100%;background:var(--white)}
  .front-panel{position:absolute;left:428px;top:0;right:0;height:100%;background:var(--black)}

  .brand-name--front{position:absolute;left:35px;top:20px;color:var(--white);font-weight:600;line-height:1}
  .brand-name--front .brand-word{display:block;font-size:40px;letter-spacing:1.5px}
  .brand-name--front .brand-sub{display:block;font-size:16px;letter-spacing:1.8px;margin-top:10px}

  .person{position:absolute;left:34px;top:126px}
  .person__name{font-weight:800;font-size:29px;color:var(--black);line-height:1.1}
  .person__role{font-weight:400;font-size:30px;color:var(--black);line-height:1.2;margin-top:2px}

  .contacts{position:absolute;left:31px;top:244px;list-style:none}
  .contact{display:flex;align-items:center;height:36px;color:var(--white);font-size:19px;font-weight:400}
  .contact__icon{width:24px;height:24px;margin-right:12px;flex:none}

  .cone-art{position:absolute;left:300px;top:55px;width:240px;height:262px;border-radius:10px;
            background:linear-gradient(180deg,var(--orange-light) 0%,var(--orange-pale) 45%,var(--orange-deep) 100%);
            opacity:.9}

  /* back */
  .brand-name--back{position:absolute;left:0;right:0;top:88px;text-align:center;color:var(--orange);font-weight:700;line-height:1}
  .brand-name--back .brand-word{display:block;font-size:80px;letter-spacing:2px}
  .brand-name--back .brand-sub{display:block;font-size:30px;letter-spacing:3.5px;margin-top:24px}

  .web-band{position:absolute;left:0;top:297px;width:581px;height:48px}
  .web-band__url{position:absolute;right:54px;top:297px;height:48px;line-height:48px;
                 color:var(--white);font-weight:700;font-size:22px;letter-spacing:.3px}
</style>
</head>
<body>

  <div class="side-label side-label--front">FRONT</div>
  <div class="side-label side-label--back">BACK</div>

  <section class="card card--front">
    <div class="front-divider"></div>
    <div class="front-panel"></div>

    <div class="brand-name brand-name--front">
      <span class="brand-word">QORVANE</span>
      <span class="brand-sub">MANAGEMENT LLC</span>
    </div>

    <div class="person">
      <div class="person__name">Dara Welk</div>
      <div class="person__role">CEO</div>
    </div>

    <ul class="contacts">
      <li class="contact">
        <svg class="contact__icon" viewBox="0 0 24 24" fill="none" stroke="#0b0b0b" stroke-width="1.4">
          <circle cx="12" cy="12" r="11"/>
          <path d="M12 18s-4.5-4.6-4.5-7.5a4.5 4.5 0 0 1 9 0C16.5 13.4 12 18 12 18z"/>
          <circle cx="12" cy="10.5" r="1.6"/>
        </svg>
        Name of your street
      </li>
      <li class="contact">
        <svg class="contact__icon" viewBox="0 0 24 24" fill="none" stroke="#0b0b0b" stroke-width="1.4">
          <circle cx="12" cy="12" r="11"/>
          <rect x="8.5" y="5.5" width="7" height="13" rx="1.5"/>
          <line x1="11" y1="16.5" x2="13" y2="16.5"/>
        </svg>
        +42 3024 555 019
      </li>
      <li class="contact">
        <svg class="contact__icon" viewBox="0 0 24 24" fill="none" stroke="#0b0b0b" stroke-width="1.4">
          <circle cx="12" cy="12" r="11"/>
          <rect x="6.5" y="8" width="11" height="8" rx="1"/>
          <path d="M6.5 8.5l5.5 4 5.5-4"/>
        </svg>
        DaraWelk@Qorvane.com
      </li>
    </ul>

    <div class="cone-art" role="img" aria-label="Photo of an orange traffic cone with white reflective bands"></div>
  </section>

  <section class="card card--back">
    <div class="brand-name brand-name--back">
      <span class="brand-word">QORVANE</span>
      <span class="brand-sub">MANAGEMENT LLC</span>
    </div>

    <svg class="web-band" viewBox="0 0 581 48" preserveAspectRatio="none">
      <rect x="0" y="0" width="581" height="48" fill="#0b0b0b"/>
      <polygon points="0,0 100,0 80,48 0,48" fill="#EE7325"/>
      <polygon points="44,0 54,0 34,48 24,48" fill="#ffffff"/>
      <polygon points="66,0 76,0 56,48 46,48" fill="#ffffff"/>
      <polygon points="88,0 98,0 78,48 68,48" fill="#ffffff"/>
    </svg>
    <div class="web-band__url">www.qorvanemanagement.com</div>
  </section>

</body>
</html>
```